Music video company site re-design :-)

Hi guys,

I run a small music video production company called "Northgate Clip Works".

It's the new year and I'm hoping to update our website design, but am at a bit of a loss - which is where I'm desperately hoping you can help!

I need something cool and contemporary but not utterly terrifying/confusing that your average band manager/solo artist funding their own music video for the first time, won't be put off.

If you can check out our current website (http://www.NorthgateClipWorks.example) I think that would probably help :-)

Target Market(s)

Solo music artists and managers of small groups/bands.

Industry/Entity Type

It Company

Requirements
Must have
• Clear, cool but accessible.

I'll need to be able to embed Pixora videos from our Pixora-plus account into the pages...

http://www.pixora.example/framehousefilms

I'd also like to be able to optimise the site for search engines, so we'll need text and not images with text in them.

I'd also like to include or use images from our videos throughout the site, so if you can include as many of these as possible that would be great.

I've uploaded a zip file with them in, how they are used is up to you guys, but the more the merrier.
Should not have
• Images of cameras, lights, clapper boards etc...

No bloody Times New Roman unless you are really reinventing that wheel or trying to make it look like my nan made my website with clip art.

Also, no god damn emoticons ;-)

```html
<!DOCTYPE html>
<html lang="en">
<head>
<meta charset="utf-8">
<title>Northgate Clip Works</title>
<link rel="stylesheet" href="https://fonts.googleapis.com/css2?family=Arimo:wght@400;700&display=swap">
<style>
:root{
  --bg:#0c0c0c;
  --bg-mid:#2a2a2a;
  --panel:#353535;
  --panel-dark:#1e1e1e;
  --bar:#262626;
  --text:#ffffff;
  --muted:#9a9a9a;
  --nav-text:#8c8c8c;
  --red:#e01010;
  --cyan:#35d3e0;
  --line:#5a5a5a;
}
*{box-sizing:border-box;margin:0;padding:0}
html,body{width:1200px;height:1200px;overflow:hidden}
body{
  font-family:"Arimo",Arial,sans-serif;color:var(--text);
  background:
    linear-gradient(180deg,#000 0,#0a0a0a 420px,#1b1b1b 460px,#2e2e2e 720px,#262626 870px,#141414 890px,#2a2a2a 1000px,#1a1a1a 1120px,#101010 1200px);
  position:relative;
}
.site{position:relative;width:1200px;height:1200px}
.abs{position:absolute}

.brand{left:47px;top:34px;font-size:44px;font-weight:700;color:var(--red);letter-spacing:-1.5px;line-height:50px}

.main-nav{left:35px;top:111px;width:1130px;height:34px;border-radius:8px 8px 0 0;
  background:linear-gradient(180deg,#3a3a3a,#1c1c1c);display:flex;align-items:center;font-size:13px}
.main-nav a{color:var(--nav-text);text-decoration:none;text-align:center;border-right:1px solid #111;box-shadow:1px 0 0 #444;line-height:16px}
.main-nav a.current{color:#fff}
.main-nav a:last-child{border:none;box-shadow:none;margin-left:auto;padding-right:22px}

.hero{left:35px;top:145px;width:832px;height:273px;border-radius:0 0 0 8px;overflow:hidden;
  background:linear-gradient(110deg,#3d4660 0,#6b2a22 30%,#b3382a 45%,#3a2a26 60%,#c9c4bd 78%,#3b3b3b 100%)}
.hero-caption{left:0;bottom:0;width:100%;height:30px;background:rgba(30,30,30,.75);font-size:14px;line-height:30px;padding-left:13px}

.news{left:867px;top:145px;width:298px;height:273px;background:linear-gradient(180deg,#303030,#242424);border-radius:0 0 8px 0;padding:12px 22px 0 15px}
.news h2{font-size:15px;font-weight:700;padding-bottom:10px;border-bottom:1px solid #555;margin-bottom:12px}
.news ul{list-style:none}
.news li{position:relative;font-size:12px;line-height:16px;padding:0 0 8px 21px;margin-bottom:9px;border-bottom:1px dashed #777}
.news li:last-child{border:none}
.news li::before{content:"";position:absolute;left:4px;top:5px;border-left:4px solid var(--cyan);border-top:3px solid transparent;border-bottom:3px solid transparent}

.welcome{left:48px;top:480px;width:480px}
.welcome h1{font-size:20px;font-weight:400;margin-bottom:14px}
.welcome p{font-size:14px;line-height:19px;margin-bottom:19px}

.player{left:610px;top:481px;width:555px;height:374px;border:1px solid #666;border-radius:10px;background:#1a1a1a}
.player-screen{left:15px;top:15px;width:526px;height:343px;background:radial-gradient(ellipse at 60% 60%,#6e8a84,#2c3a38 60%,#101816)}
.player-controls{left:15px;top:307px;width:496px;height:31px;border-radius:3px;background:linear-gradient(180deg,#9a9a9a,#5e5e5e)}

.feature{top:905px;width:365px;height:208px;border-radius:8px;background:#3c3c3c;overflow:hidden;box-shadow:0 2px 4px #000}
.feature h3{height:32px;background:linear-gradient(180deg,#3b3b3b,#1d1d1d);font-size:13.5px;font-weight:700;line-height:32px;padding-left:13px}
.feature .thumb{height:99px}
.feature p{font-size:13.5px;line-height:17px;padding:6px 14px 0;text-align:justify}
.read-more{right:0;bottom:0;width:96px;height:25px;border-radius:8px 0 0 0;background:#1a1a1a;font-size:11px;line-height:25px;text-align:center;color:#fff}

.footer-rule{left:35px;top:1133px;width:1130px;height:1px;background:#3c3c3c}
.footer-brand{left:48px;top:1155px;font-size:19px;font-weight:700;color:#7a7a7a;letter-spacing:-.5px}
.footer-nav{left:276px;top:1152px;font-size:11px;display:flex;gap:23px}
.footer-nav a{color:#d0d0d0;text-decoration:none}
.footer-nav a.current{color:var(--red)}
.copyright{left:276px;top:1169px;font-size:11px;color:#d0d0d0}
</style>
</head>
<body>
<div class="site">
  <div class="abs brand">Northgate Clip Works</div>

  <nav class="abs main-nav">
    <a class="current" href="#" style="width:167px">homepage</a>
    <a href="#" style="width:167px">music video</a>
    <a href="#" style="width:174px">promo feature</a>
    <a href="#" style="width:191px">band site design</a>
    <a href="#" style="width:132px">prices</a>
    <a href="#">Contact Us</a>
  </nav>

  <div class="abs hero" role="img" aria-label="Slide photo from a music video: boxers in a ring corner">
    <div class="abs hero-caption">Image slide name</div>
  </div>

  <aside class="abs news">
    <h2>News:</h2>
    <ul>
      <li>Lorem ipsum dolor sit amet, consectetuer adipiscing elit. Donec molestie. Sed aliquam sem ut arcu. Phasellus.</li>
      <li>Lorem ipsum dolor sit amet.</li>
      <li>Lorem ipsum dolor sit amet, consectetuer adipiscing elit. Donec molestie. Sed aliquam sem ut arcu. Phasellus.</li>
      <li>Lorem ipsum dolor sit amet, consectetuer adipiscing elit. Donec molestie.</li>
    </ul>
  </aside>

  <section class="abs welcome">
    <h1>Welcome to NorthgateClipWorks.example</h1>
    <p>Lorem ipsum dolor sit amet, consectetuer adipiscing elit. Donec molestie. Sed aliquam sem ut arcu. Phasellus sollicitudin Lorem ipsum dolor sit amet consectetuer adipiscing elit. Donec molestie. Sed aliquam sem ut arcu. Phasellus sollicitudin.</p>
    <p>Lorem ipsum dolor sit amet, consectetuer adipiscing elit. Donec molestie. Sed aliquam sem ut arcu. Phasellus sollicitudin Lorem ipsum dolor.</p>
    <p>Lorem ipsum dolor sit amet, consectetuer adipiscing elit. Donec molestie. Sed aliquam sem ut arcu. Phasellus sollicitudin Lorem ipsum dolor sit amet consectetuer adipiscing elit. Donec molestie. Sed aliquam sem ut arcu. Phasellus sollicitudin.</p>
    <p>Lorem ipsum dolor sit amet</p>
  </section>

  <div class="abs player">
    <div class="abs player-screen" role="img" aria-label="Embedded video still: riders on a BMX in a dark tunnel">
      <div class="abs player-controls">
        <svg width="496" height="31" viewBox="0 0 496 31">
          <polygon points="12,9 12,22 22,15.5" fill="#3a3a3a"/>
          <rect x="37" y="10" width="3" height="11" fill="#777"/><rect x="43" y="10" width="3" height="11" fill="#777"/>
          <rect x="60" y="11" width="9" height="9" fill="#3a3a3a"/>
          <rect x="82" y="4" width="276" height="22" fill="#d4d4d4" stroke="#eee"/>
          <rect x="82" y="14" width="276" height="2" fill="#888"/>
          <polygon points="263,18 268,13 273,18 273,23 263,23" fill="#fff"/>
          <polygon points="372,12 376,12 381,8 381,23 376,19 372,19" fill="#111"/>
          <path d="M384 11 q3 4.5 0 9" stroke="#111" fill="none" stroke-width="1.5"/>
          <polygon points="398,23 480,23 480,10" fill="#eee"/>
          <polygon points="425,18 430,13 435,18 435,23 425,23" fill="#fff" stroke="#888" stroke-width=".5"/>
        </svg>
      </div>
    </div>
  </div>

  <article class="abs feature" style="left:35px">
    <h3>Music Video</h3>
    <div class="thumb" role="img" aria-label="Video still: singer in a hat at a microphone under stage lights" style="background:linear-gradient(90deg,#6a3a2a,#c58a6a 30%,#3a2a24 60%,#8a5a44)"></div>
    <p>Lorem ipsum dolor sit amet, consectetuer adipiscing elit. Donec molestie. Sed aliquam sem ut arcu. Phasellus sollicitudin...</p>
    <div class="abs read-more">read more</div>
  </article>

  <article class="abs feature" style="left:419px">
    <h3>Promo Feature</h3>
    <div class="thumb" role="img" aria-label="Video still: presenter standing in a green screen studio" style="background:linear-gradient(90deg,#2a2a3a,#5f9a3a 30%,#6cae3e 50%,#e8e8e8 65%,#2a2a2a)"></div>
    <p>Lorem ipsum dolor sit amet, consectetuer adipiscing elit. Donec molestie...</p>
    <div class="abs read-more">read more</div>
  </article>

  <article class="abs feature" style="left:801px">
    <h3>Band Site Design</h3>
    <div class="thumb" role="img" aria-label="Video still: producer working at a mixing desk" style="background:linear-gradient(90deg,#3a2a22,#6a6a6a 35%,#9a9a9a 60%,#4a4a4a)"></div>
    <p>Lorem ipsum dolor sit amet, consectetuer adipiscing elit. Donec molestie. Sed aliquam sem ut arcu...</p>
    <div class="abs read-more">read more</div>
  </article>

  <div class="abs footer-rule"></div>
  <div class="abs footer-brand">Northgate Clip Works</div>
  <nav class="abs footer-nav">
    <a class="current" href="#">homepage</a>
    <a href="#">music video</a>
    <a href="#">promo feature</a>
    <a href="#">band site design</a>
    <a href="#">price</a>
    <a href="#">contact us</a>
  </nav>
  <div class="abs copyright">copyright © 2011 - Northgate Clip Works</div>
</div>
</body>
</html>
```